Website for a dog poop removal service.

The Fernwick Folks specializes in professional and hassle-free pet waste removal services, ensuring your yard stays clean, fresh, and safe for your family and pets. We take care of the dirty work, so you don’t have to, offering reliable, scheduled cleanups tailored to your needs. Let us help you reclaim your time and enjoy a spotless, stress-free outdoor space!
We will need the winning website to be transferred to our domain located at Valtorix. We would like to have the following web pages.
Home
About
Services
Contact Us
Client Portal
FAQ
Blog
Free Quote
The Free Quote webpage and client portal will need to be integrated with the following our account on the following website: tallowfen.com

```html
<!DOCTYPE html>
<html lang="en">
<head>
<meta charset="utf-8">
<title>The Fernwick Folks – Pet Waste Removal</title>
<link href="https://fonts.googleapis.com/css2?family=Outfit:wght@400;500;600;700;800&family=Lato:wght@400;700&display=swap" rel="stylesheet">
<style>
:root{
  --green:#6db33f;
  --green-dark:#5a9a30;
  --brown:#c49a6c;
  --ink:#151515;
  --text:#555;
  --grey:#f1f1f1;
  --white:#fff;
  --footer:#1b1b1b;
}
*{box-sizing:border-box;margin:0;padding:0}
html,body{width:1200px;height:4274px;overflow:hidden}
body{position:relative;background:var(--white);font-family:"Lato",sans-serif;color:var(--ink)}
.abs{position:absolute}
.head{font-family:"Outfit",sans-serif}
.photo{position:absolute;overflow:hidden}

/* header */
.brand{left:112px;top:38px;display:flex;align-items:center;gap:12px}
.brand-dot{width:54px;height:54px;border-radius:50%;background:var(--green)}
.brand-name{font-family:"Outfit",sans-serif;font-weight:700;font-size:22px;line-height:1.05;color:var(--ink);text-transform:uppercase}
.contact-item{display:flex;align-items:center;gap:14px}
.icon-circle{width:40px;height:40px;border-radius:50%;background:var(--green);display:flex;align-items:center;justify-content:center}
.contact-item b{display:block;font-family:"Outfit",sans-serif;font-size:15px;font-weight:600}
.contact-item span{font-size:15px;color:#444}
.social{display:flex;gap:13px}
.social i{display:block;width:38px;height:38px;border-radius:50%;border:1.5px solid var(--brown)}
.social i.on{background:var(--green);border-color:var(--green)}
.nav{left:370px;top:65px;width:830px;height:48px}
.nav ul{position:absolute;inset:0;display:flex;list-style:none;align-items:center;padding-left:50px;gap:0}
.nav li{font-family:"Outfit",sans-serif;font-weight:600;font-size:15px;color:var(--white);padding:0 19px;height:48px;line-height:48px}
.nav li.active{background:var(--green)}

/* hero */
.hero-title{left:110px;top:200px;font-family:"Outfit",sans-serif;font-weight:800;font-size:54px;line-height:58px;color:var(--ink)}
.hero-title em{font-style:normal;font-weight:500;color:var(--green)}
.hero-sub{left:111px;top:385px;width:480px;font-size:24px;line-height:34px;color:#555}
.btn{position:absolute;display:flex;align-items:center;justify-content:center;border-radius:30px;font-family:"Outfit",sans-serif;font-weight:600;font-size:16px;color:var(--white);text-transform:uppercase}
.btn-green{background:var(--green)}
.btn-brown{background:var(--brown)}
.btn-white{background:var(--white);color:var(--ink)}

/* section headings */
.eyebrow{position:absolute;left:0;width:1200px;text-align:center;font-size:14px;color:var(--brown);text-transform:uppercase}
.eyebrow::before,.eyebrow::after{content:"";display:inline-block;width:34px;height:2px;background:var(--brown);vertical-align:middle;margin:0 10px}
.title{position:absolute;left:0;width:1200px;text-align:center;font-family:"Outfit",sans-serif;font-size:46px;font-weight:400;text-transform:uppercase}
.title b{font-weight:800}

/* services */
.service-card{position:absolute;top:835px;width:228px;height:275px;border-radius:22px 22px 0 0}
.service-label{position:absolute;top:1069px;height:50px;border-radius:8px;background:var(--white);box-shadow:0 4px 12px rgba(0,0,0,.15);display:flex;align-items:center;justify-content:center;font-family:"Outfit",sans-serif;font-weight:600;font-size:14px}
.service-label.active{background:var(--brown);color:var(--white);border:2px solid var(--white)}
.arrow{position:absolute;width:38px;height:38px;border-radius:50%;display:flex;align-items:center;justify-content:center}
.arrow-outline{border:1.5px solid var(--white)}
.arrow-dark{border:1.5px solid var(--ink)}
.arrow-fill{background:var(--green)}

/* about */
.about-eyebrow{left:601px;top:1238px;font-size:14px;color:var(--white)}
.about-eyebrow::after{content:"";display:inline-block;width:34px;height:2px;background:var(--white);vertical-align:middle;margin-left:8px}
.about-title{left:601px;top:1262px;font-family:"Outfit",sans-serif;font-size:46px;color:var(--white)}
.about-text{left:601px;top:1334px;width:490px;font-size:17px;line-height:25.5px;color:var(--white)}

/* why */
.why-item{position:absolute;width:300px}
.why-item h3{font-family:"Outfit",sans-serif;font-weight:600;font-size:20px;text-transform:uppercase;margin-bottom:6px}
.why-item p{font-size:18px;line-height:25px;color:#666}
.why-item.right{text-align:right}
.why-icon{position:absolute;width:64px;height:64px;border-radius:50%;background:var(--white);box-shadow:0 3px 12px rgba(0,0,0,.15);display:flex;align-items:center;justify-content:center}

/* faq */
.faq-eyebrow{left:111px;top:2494px;font-size:14px;color:var(--brown)}
.faq-eyebrow::after{content:"";display:inline-block;width:34px;height:2px;background:var(--brown);vertical-align:middle;margin-left:8px}
.faq-title{left:111px;top:2520px;font-family:"Outfit",sans-serif;font-size:46px;line-height:52px;text-transform:uppercase}
.faq-item{position:absolute;left:111px;width:532px;border-radius:30px;background:#e6e6e6;padding:0 20px;font-family:"Outfit",sans-serif;font-size:16px;text-transform:uppercase;display:flex;align-items:center;justify-content:space-between}
.faq-item .pm{width:28px;height:28px;border-radius:50%;background:var(--ink);color:var(--white);display:flex;align-items:center;justify-content:center;font-size:22px;line-height:1}
.faq-open{background:var(--green);color:var(--white);display:block;padding:14px 20px;border-radius:18px}
.faq-open .q{display:flex;justify-content:space-between;font-weight:500}
.faq-open p{font-family:"Lato",sans-serif;text-transform:none;font-size:15px;line-height:22px;margin-top:8px}

/* blog */
.blog-card{position:absolute;top:3272px;width:316px;height:433px;border-radius:24px;background:var(--white);box-shadow:0 2px 14px rgba(0,0,0,.08);overflow:hidden}
.blog-card .img{height:190px}
.blog-card h4{margin:30px 14px 0;font-family:"Outfit",sans-serif;font-weight:600;font-size:16px;line-height:23px;text-transform:uppercase}
.blog-card p{margin:14px 14px 0;font-size:15.5px;line-height:23.5px;color:#666}
.blog-card a{display:block;margin:10px 14px 0;font-family:"Outfit",sans-serif;font-weight:600;font-size:16px;color:var(--brown);text-decoration:underline}

/* footer */
.foot-col h5{font-family:"Outfit",sans-serif;font-weight:600;font-size:21px;color:var(--white);text-transform:uppercase;margin-bottom:14px}
.foot-col li{list-style:none;font-family:"Outfit",sans-serif;font-size:15px;color:var(--white);text-transform:uppercase;height:32px}
.foot-contact{display:flex;gap:20px;margin-bottom:24px;color:var(--white)}
.foot-contact b{display:block;font-family:"Outfit",sans-serif;font-size:15px;font-weight:600}
.foot-contact span{font-size:15px;text-transform:uppercase;line-height:22px}
.copyright{left:0;top:4238px;width:1200px;text-align:center;font-size:15px;color:var(--white)}
</style>
</head>
<body>

<!-- HEADER -->
<header>
  <div class="abs brand">
    <div class="brand-dot"></div>
    <div class="brand-name">The Fernwick<br>Folks</div>
  </div>
  <div class="abs contact-item" style="left:375px;top:12px">
    <div class="icon-circle"><svg width="18" height="18" viewBox="0 0 24 24"><path fill="#fff" d="M6.6 10.8a15 15 0 0 0 6.6 6.6l2.2-2.2c.3-.3.7-.4 1-.2 1.1.4 2.3.6 3.6.6.6 0 1 .4 1 1V20c0 .6-.4 1-1 1A17 17 0 0 1 3 4c0-.6.4-1 1-1h3.5c.6 0 1 .4 1 1 0 1.3.2 2.5.6 3.6.1.3 0 .7-.2 1z"/></svg></div>
    <div><b>PHONE NO:</b><span>+1(888) 888 8888</span></div>
  </div>
  <div class="abs contact-item" style="left:632px;top:12px">
    <div class="icon-circle"><svg width="18" height="18" viewBox="0 0 24 24"><path fill="#fff" d="M3 6h18v12H3z"/><path fill="none" stroke="#6db33f" stroke-width="1.8" d="M3 6l9 7 9-7"/></svg></div>
    <div><b>EMAIL:</b><span>INFO@FERNWICKFOLKS.COM</span></div>
  </div>
  <div class="abs social" style="left:943px;top:13px" aria-label="Social links">
    <i class="on"></i><i></i><i></i>
  </div>
  <nav class="abs nav">
    <svg class="abs" style="left:0;top:0" width="830" height="48"><polygon points="0,0 830,0 830,48 30,48" fill="#c49a6c"/><polygon points="0,0 115,0 115,48 30,48" fill="#6db33f"/></svg>
    <ul>
      <li class="active" style="margin-left:-20px">HOME</li><li>ABOUT</li><li>SERVICES</li><li>CLIENT PORTAL</li><li>FAQ</li><li>BLOG</li><li>CONTACT US</li>
    </ul>
  </nav>
</header>

<!-- HERO -->
<section>
  <h1 class="abs hero-title">KEEPING YOUR <em>YARD</em><br><em>LEAN, FRESH,</em>AND<br>HASSLE-FREE!</h1>
  <p class="abs hero-sub">Professional pet waste removal services tailored to your needs.</p>
  <div class="btn btn-green" style="left:111px;top:466px;width:351px;height:58px">Schedule your first cleanup now</div>
  <div class="btn btn-brown" style="left:111px;top:536px;width:247px;height:56px">Get a free quote today</div>
  <div class="photo" role="img" aria-label="Golden retriever smiling with a family in the background" style="left:678px;top:124px;width:497px;height:497px;border-radius:50%;background:radial-gradient(circle at 60% 50%,#c8843f,#8a6a48 60%,#5d6b3c)"></div>
  <div class="photo" role="img" aria-label="Man and child sitting on grass with a small fluffy dog" style="left:581px;top:388px;width:276px;height:276px;border-radius:50%;border:3px solid #fff;background:radial-gradient(circle at 55% 55%,#cfcac2,#8d9477 55%,#5f7545)"></div>
</section>

<!-- SERVICES -->
<section>
  <div class="eyebrow" style="top:715px">What we do</div>
  <h2 class="title" style="top:738px"><b>Our</b> Services</h2>
  <svg class="abs" style="left:0;top:900px" width="1200" height="860">
    <path d="M0 60 Q 80 20 120 40 L 1200 40 L 1200 100 Q 1100 120 1080 180 L 1200 180 L 1200 610 Q 1100 600 990 640 Q 800 720 600 680 Q 540 660 520 640 Q 400 700 240 760 L 0 760 Z" fill="#6db33f"/>
  </svg>
  <div class="arrow arrow-outline" style="left:39px;top:947px"><svg width="12" height="12" viewBox="0 0 12 12"><path d="M8 1 3 6l5 5" fill="none" stroke="#fff" stroke-width="1.8"/></svg></div>
  <div class="arrow arrow-fill" style="left:1126px;top:947px;border:1.5px solid #fff"><svg width="12" height="12" viewBox="0 0 12 12"><path d="M4 1l5 5-5 5" fill="none" stroke="#fff" stroke-width="1.8"/></svg></div>
  <div class="service-card photo" role="img" aria-label="Person scooping dog waste on a lawn" style="left:112px;background:linear-gradient(#3d4a2b,#6f7f52 60%,#aab89a)"></div>
  <div class="service-card photo" role="img" aria-label="Poodle on grass beside a hand with a green waste bag" style="left:362px;background:linear-gradient(#5f8a36,#b49a70 45%,#7fa84b)"></div>
  <div class="service-card photo" role="img" aria-label="Business handshake" style="left:613px;background:linear-gradient(135deg,#f4f5f7,#d9dde3 60%,#c9b8a6)"></div>
  <div class="service-card photo" role="img" aria-label="Small terrier running on grass" style="left:862px;background:linear-gradient(#86a25a,#bfa58a 45%,#4f7f2a)"></div>
  <div class="service-label" style="left:125px;width:200px">WEEKLY CLEANUPS</div>
  <div class="service-label active" style="left:376px;width:200px">ONE-TIME CLEANUPS</div>
  <div class="service-label" style="left:626px;width:200px">CUSTOM SCHEDULES</div>
  <div class="service-label" style="left:875px;width:200px">COMMERCIAL SERVICES</div>
</section>

<!-- ABOUT -->
<section>
  <svg class="abs" style="left:0;top:1235px" width="565" height="500">
    <path d="M0 60 Q 160 -20 360 20 Q 560 70 555 260 Q 550 420 520 480 Q 480 520 440 430 Q 380 340 200 400 Q 80 440 0 400 Z" fill="none" stroke="#fff" stroke-width="3"/>
  </svg>
  <div class="photo" role="img" aria-label="Golden retriever in a sunny meadow with people behind" style="left:0;top:1252px;width:548px;height:470px;border-radius:0 300px 200px 0 / 0 260px 240px 0;background:radial-gradient(circle at 35% 50%,#d49a52,#a9864e 50%,#7c8c3b)"></div>
  <div class="abs about-eyebrow">WHO WE ARE</div>
  <h2 class="abs about-title"><b style="font-weight:800">ABOUT</b> US</h2>
  <p class="abs about-text">We're passionate about making life easier for pet owners. Our professional team is dedicated to ensuring your yard stays clean, healthy, and stress-free. With flexible scheduling, affordable rates, and top-notch customer service, we make pet ownership even more enjoyable.ensuring your yard stays clean, fresh, and safe</p>
  <div class="btn btn-white" style="left:601px;top:1507px;width:142px;height:54px">Read more</div>
  <div class="photo" role="img" aria-label="Golden retriever and pug lying on the grass" style="left:800px;top:1530px;width:400px;height:205px;background:linear-gradient(90deg,rgba(212,160,96,0) 0%,#d6a566 20%,#c89657 55%,#8a6d4f 80%,#5e6c3a)"></div>
</section>

<!-- WHY CHOOSE US -->
<section>
  <div class="eyebrow" style="top:1820px">The Fernwick Folks</div>
  <h2 class="title" style="top:1843px"><b>Why</b> Choose Us</h2>
  <svg class="abs" style="left:430px;top:1930px" width="340" height="310">
    <path d="M40 260 A 160 160 0 1 1 300 260" fill="none" stroke="#6db33f" stroke-width="4"/>
  </svg>
  <div class="photo" role="img" aria-label="Cartoon dog mascot with scooper" style="left:500px;top:1955px;width:190px;height:235px;border-radius:50% 50% 20px 20px;background:radial-gradient(circle at 50% 40%,#f2f2f2,#e0e6da 70%,#cfe3bd)"></div>
  <div class="why-icon" style="left:446px;top:1973px"><svg width="30" height="30" viewBox="0 0 24 24"><path d="M12 3l2.5 5 5.5.8-4 3.9.9 5.5L12 15.6 7.1 18.2 8 12.7 4 8.8l5.5-.8z" fill="#c49a6c"/></svg></div>
  <div class="why-icon" style="left:690px;top:1973px"><svg width="30" height="30" viewBox="0 0 24 24"><circle cx="12" cy="12" r="9" fill="#c49a6c"/><path d="M7.5 12.5l3 3 6-6" fill="none" stroke="#fff" stroke-width="2.2"/></svg></div>
  <div class="why-icon" style="left:424px;top:2102px"><svg width="30" height="30" viewBox="0 0 24 24"><path d="M12 20c-4-3-7-6-7-10a4 4 0 0 1 7-2 4 4 0 0 1 7 2c0 4-3 7-7 10z" fill="#c49a6c"/></svg></div>
  <div class="why-icon" style="left:712px;top:2102px"><svg width="30" height="30" viewBox="0 0 24 24"><circle cx="12" cy="12" r="4" fill="none" stroke="#c49a6c" stroke-width="3"/><circle cx="12" cy="12" r="9" fill="none" stroke="#c49a6c" stroke-width="2" stroke-dasharray="3 2"/></svg></div>
  <div class="why-item right" style="left:124px;top:1955px"><h3>Reliable Service</h3><p>Always on time, always thorough.</p></div>
  <div class="why-item" style="left:776px;top:1955px"><h3>Satisfaction Guaranteed</h3><p>We're not happy unless you're happy!</p></div>
  <div class="why-item right" style="left:110px;top:2095px;width:300px"><h3>Pet &amp; Eco-Friendly</h3><p>Safe disposal methods and eco-conscious practices.</p></div>
  <div class="why-item" style="left:795px;top:2090px"><h3>Locally Owned &amp; Operated</h3><p>Supporting our community, one yard at a time.</p></div>
  <div class="btn btn-green" style="left:529px;top:2215px;width:142px;height:57px">Learn more</div>
</section>

<!-- FAQ -->
<section>
  <svg class="abs" style="left:0;top:2360px" width="1200" height="710">
    <path d="M0 130 Q 600 -120 1200 130 L 1200 570 Q 600 830 0 570 Z" fill="#f1f1f1"/>
    <path d="M0 140 Q 600 -110 1200 140" fill="none" stroke="#6db33f" stroke-width="4"/>
    <path d="M0 560 Q 600 820 1200 560" fill="none" stroke="#6db33f" stroke-width="4"/>
  </svg>
  <div class="photo" role="img" aria-label="Small fluffy dog running" style="left:985px;top:2270px;width:175px;height:185px;border-radius:40%;background:radial-gradient(circle,#b87a3e,#d19a5e 50%,rgba(255,255,255,0) 72%)"></div>
  <div class="abs faq-eyebrow">FAQ FOR OUR DOG POOP REMOVAL SERVICE</div>
  <h2 class="abs faq-title"><b style="font-weight:800">Frequently Asked</b><br>Questions</h2>
  <div class="faq-item" style="top:2650px;height:60px">What does your dog poop removal service include?<span class="pm">+</span></div>
  <div class="faq-item" style="top:2725px;height:60px">Do you service all yard sizes?<span class="pm">+</span></div>
  <div class="faq-item faq-open" style="top:2797px;height:100px">
    <div class="q"><span>How often can I schedule your services?</span><span>–</span></div>
    <p>A3: You can schedule services weekly, bi-weekly, or on a one-time basis. Custom schedules are also available.</p>
  </div>
  <div class="btn btn-green" style="left:500px;top:2913px;width:143px;height:58px">Learn more</div>
  <div class="abs" style="left:678px;top:2490px;width:463px;height:463px;border-radius:50%;border:3px solid #6db33f"></div>
  <div class="photo" role="img" aria-label="Smiling woman hugging a golden retriever in a garden" style="left:687px;top:2499px;width:445px;height:445px;border-radius:50%;background:radial-gradient(circle at 50% 60%,#e8d4b4,#b6894f 45%,#6e7d42)"></div>
</section>

<!-- BLOG -->
<section>
  <div class="eyebrow" style="top:3157px">Our blog</div>
  <h2 class="title" style="top:3180px"><b>Our</b> Latest News</h2>
  <div class="arrow arrow-dark" style="left:39px;top:3474px"><svg width="12" height="12" viewBox="0 0 12 12"><path d="M8 1 3 6l5 5" fill="none" stroke="#151515" stroke-width="1.8"/></svg></div>
  <div class="arrow arrow-fill" style="left:1126px;top:3474px"><svg width="12" height="12" viewBox="0 0 12 12"><path d="M4 1l5 5-5 5" fill="none" stroke="#fff" stroke-width="1.8"/></svg></div>
  <article class="blog-card" style="left:111px">
    <div class="img" role="img" aria-label="Golden retriever with a family in a park" style="background:linear-gradient(135deg,#dcbf8e,#c7a06a 45%,#6f8c4a)"></div>
    <h4>Lorem ipsum dolor sitametolor, consectetur adipiscing</h4>
    <p>Lorem ipsum dolor sit amet,ncteur isi elito eiusmod tempor nt ut labore et dolore magnaqua. Utm ad minimveiam, quis nostru sit amet,ncteur.</p>
    <a>READ MORE</a>
  </article>
  <article class="blog-card" style="left:443px">
    <div class="img" role="img" aria-label="Person with a dog at sunset" style="background:linear-gradient(135deg,#f0c070,#c98a3e 50%,#5b4a2e)"></div>
    <h4>Lorem ipsum dolor sitametolor, consectetur adipiscing</h4>
    <p>Lorem ipsum dolor sit amet,ncteur isi elito eiusmod tempor nt ut labore et dolore magnaqua. Utm ad minimveiam, quis nostru sit amet,ncteur.</p>
    <a>READ MORE</a>
  </article>
  <article class="blog-card" style="left:773px">
    <div class="img" role="img" aria-label="Person cleaning up after a white dog on a lawn" style="background:linear-gradient(#6d8c4e,#9fb07a 50%,#5f8a34)"></div>
    <h4>Lorem ipsum dolor sitametolor, consectetur adipiscing</h4>
    <p>Lorem ipsum dolor sit amet,ncteur isi elito eiusmod tempor nt ut labore et dolore magnaqua. Utm ad minimveiam, quis nostru sit amet,ncteur.</p>
    <a>READ MORE</a>
  </article>
</section>

<!-- FOOTER -->
<footer>
  <svg class="abs" style="left:0;top:3800px" width="1200" height="474">
    <path d="M0 180 Q 600 -80 1200 180 L 1200 474 L 0 474 Z" fill="#1b1b1b"/>
    <path d="M0 180 Q 600 -80 1200 180" fill="none" stroke="#6db33f" stroke-width="4"/>
    <line x1="111" y1="422" x2="1090" y2="422" stroke="#444" stroke-width="1"/>
  </svg>
  <div class="abs brand" style="left:110px;top:3960px">
    <div class="brand-dot" style="width:60px;height:60px"></div>
    <div class="brand-name" style="color:#fff;font-size:26px">The Fernwick<br>Folks</div>
  </div>
  <div class="abs foot-col" style="left:462px;top:3925px">
    <h5>Quick Links</h5>
    <ul><li>Home</li><li>About Us</li><li>Services</li><li>Client Portal</li><li>FAQ</li><li>Blog</li><li>Contact Us</li></ul>
  </div>
  <div class="abs foot-col" style="left:650px;top:3923px">
    <h5>Contact Us</h5>
    <div class="foot-contact"><div class="icon-circle"><svg width="18" height="18" viewBox="0 0 24 24"><path fill="#fff" d="M6.6 10.8a15 15 0 0 0 6.6 6.6l2.2-2.2c.3-.3.7-.4 1-.2 1.1.4 2.3.6 3.6.6.6 0 1 .4 1 1V20c0 .6-.4 1-1 1A17 17 0 0 1 3 4c0-.6.4-1 1-1h3.5c.6 0 1 .4 1 1 0 1.3.2 2.5.6 3.6.1.3 0 .7-.2 1z"/></svg></div><div><b>PHONE NO:</b><span>+1(888) 888 8888</span></div></div>
    <div class="foot-contact"><div class="icon-circle"><svg width="18" height="18" viewBox="0 0 24 24"><path fill="#fff" d="M3 6h18v12H3z"/><path fill="none" stroke="#6db33f" stroke-width="1.8" d="M3 6l9 7 9-7"/></svg></div><div><b>EMAIL:</b><span>INFO@FERNWICKFOLKS.COM</span></div></div>
    <div class="foot-contact"><div class="icon-circle"><svg width="18" height="18" viewBox="0 0 24 24"><path fill="#fff" d="M12 2a7 7 0 0 0-7 7c0 5 7 13 7 13s7-8 7-13a7 7 0 0 0-7-7zm0 9.5A2.5 2.5 0 1 1 12 6.5a2.5 2.5 0 0 1 0 5z"/></svg></div><div><b>LOCATION:</b><span>Lorem ipsum dolor sit<br>consectetur,USA</span></div></div>
  </div>
  <div class="abs foot-col" style="left:936px;top:3923px">
    <h5>Follow Us</h5>
    <div class="social" aria-label="Social links"><i class="on"></i><i style="border-color:#fff"></i><i style="border-color:#fff"></i></div>
  </div>
  <div class="abs copyright">© 2024 The Fernwick Folks. All Rights Reserved</div>
</footer>

</body>
</html>
```